Board menu for "Pan Dorado" food truck

Summary
**********************************
We need a menu design for a food truck. The menu will be printed and placed in the food truck side, so that customers can read it while standing one or two meters away from it. The size of the printed menu should be (width x height): 108cm x 70cm. The food truck is located in Panama and the menu language is Spanish.

Menu Sections
**************************************
The menu is divided in the following 5 sections:

1. Main Courses: This section should take most of the menu space. There are 5 menu items in this section. Each item has a Name, Description, Picture, Price (of item alone), and Price (of item in combo). Please note that for all items, combo means adding one beverage and one side. The added price is $1.50 to make any main course a combo. So it might we better to say “make it a combo for +$1.50” versus say “alone $5.50, in combo $7.00”.

2. Side Orders: This section has 2 menu items. Each item has a Name and Price. There are no pictures for this section or items.

3. Soups: This section has a Picture and Description for the entire section plus 2 menu items. Each menu item has a Name and Price.

4. Bakery: This section has a Picture for the entire section plus 5 menu items. Each item has a Name and a Price.

5. Beverages: This section has 5 menu items. Each menu item has a Name and a Price. There are no pictures for this section or items.

Attachments
*******************************************
We are attaching a zip file with picture of the exterior of the food truck. The menu will go in the space between the food truck’s window and the light switch, leaving ample space between those boundaries and the menu. The trash can shown in the picture has been relocated so it will not obstruct the menu view.

The zip file also contains the pictures for the 5 menu items in the Main Courses section, the picture for the Soups section, and the picture for the Bakery section (the bakery picture is provided as a place holder. We will provide a better bakery picture to the winning design to replace this one). For information purposes, the zip file also contains the food truck logo. The logo will not go in the menu. The brand and social media icons will go elsewhere in the truck.

The zip file also contains the file “menu information.xlsx”. This file has the following sheets:

Sections: Contains a column with the section name in English and another one with the section name in Spanish (which should be used in the menu). For the Soups section, contains a column with the section’s Description and Picture Name. For the Bakery section, contains a column with the section’s Picture Name.

Main Courses: Contains a column for each of the following: Item Name, Item Description, Item Picture Name, Item Price, Item Price (in combo). Again, we leave it to the designer’s discretion to use +$1.50 (or similar) for the combo versus publishing the full combo price.

Side Orders: Contains columns for Item Name and Item Price.

Soups: Contains columns for Item Name and Item Price.

Bakery: Contains columns for Item Name and Item Price. In the case of the Donuts item, there is an addition column with the Available Flavors.

Beverages: Contains columns for Item Name and Item Price. In the case of the Sodas item, there is an additional column with the Available Flavors.

A note about file encoding: the excel file contains texts with Spanish language special characters. It is encoded in the Windows-1252 encoding which I think is the Excel default for Western European languages. For those having trouble with this encoding, I included a “menu information csv” folder in the zip file with all the sheets in csv format encoded using UTF-8.
Updates

Target Market(s)

The truck sells fast food to drivers commuting from Panama City to towns in the west of the city. The average customer is a middle-class professional with a car. The truck is located in one of our gas stations so most customers stop to fuel their cars and grab something to eat for the ride home.

Font styles to use
Sans Serif

Colors

Designer to choose colors to be used in the design.

Requirements
Must have
• We would like to make emphasis in the main courses. Since they required preparation, they are not displayed, unlike other items like bakery, soups and beverages that are always ready and displayed. Having their pictures and descriptions on the menu will allows the customer to quickly figure out what main courses are available.

```html
<!DOCTYPE html>
<html lang="es">
<head>
<meta charset="utf-8">
<title>Pan Dorado — Menú</title>
<link href="https://fonts.googleapis.com/css2?family=Bangers&family=Courier+Prime:wght@400;700&display=swap" rel="stylesheet">
<style>
:root{
  --bg:#f2c384;
  --bar:#4a4a4a;
  --ink:#2b2b2b;
  --brown:#4a3320;
  --frame:#5b3d1f;
  --grey:#555555;
  --white:#ffffff;
  --burst:#3d3d3d;
}
*{margin:0;padding:0;box-sizing:border-box}
html,body{width:1200px;height:778px;overflow:hidden;background:var(--bg)}
.menu{position:relative;width:1200px;height:778px;background:var(--bg);font-family:'Bangers',sans-serif;color:var(--ink)}
.abs{position:absolute}
.bar{position:absolute;background:var(--bar);display:flex;align-items:center;justify-content:center;color:var(--white);letter-spacing:1.5px;-webkit-text-stroke:1px #111;paint-order:stroke fill}
.bar::before,.bar::after{content:"";position:absolute;top:50%;width:12px;height:12px;margin-top:-6px;border-radius:50%;background:#111}
.bar::before{left:14px}.bar::after{right:14px}
.bar-title{left:322px;top:8px;width:548px;height:46px;font-size:38px;letter-spacing:2px}
.bar-title::before,.bar-title::after{width:20px;height:20px;margin-top:-10px}
.bar-section{height:35px;font-size:24px}
.dish{position:absolute;top:66px;width:196px}
.dish-price{position:absolute;left:-2px;top:0;font-size:34px;color:var(--brown);letter-spacing:1.5px}
.combo{position:absolute;left:84px;top:-2px;width:124px;height:86px;z-index:3}
.combo svg{position:absolute;inset:0}
.combo-text{position:absolute;inset:0;display:flex;flex-direction:column;align-items:center;justify-content:center;padding-top:4px;color:var(--white);line-height:.85;letter-spacing:1px;-webkit-text-stroke:1px #111;paint-order:stroke fill}
.combo-text small{font-size:22px}
.combo-text b{font-size:36px;font-weight:400}
.photo{position:absolute;z-index:1;border:6px solid var(--frame);outline:2px solid var(--frame);outline-offset:3px}
.dish .photo{left:4px;top:44px;width:184px;height:164px}
.dish-name{position:absolute;left:0;top:216px;width:196px;text-align:center;font-size:22px;letter-spacing:1.5px;font-weight:400}
.dish-desc{position:absolute;left:8px;top:243px;width:180px;text-align:center;font-family:'Courier Prime',monospace;font-size:9.5px;line-height:11px;text-transform:uppercase}
.row{position:absolute;display:flex;justify-content:space-between;color:var(--grey);letter-spacing:1px}
.side{left:88px;width:294px;font-size:28px}
.bakery{left:445px;width:320px;font-size:21px}
.drink{left:805px;width:333px;font-size:21px}
.soup{left:64px;width:344px;font-size:21px;line-height:19px}
.soup span:last-child{font-size:25px}
.note{position:absolute;font-family:'Courier Prime',monospace;font-size:9.5px;text-transform:uppercase;color:var(--ink)}
.brand{position:absolute;left:842px;top:676px;display:flex;align-items:center;gap:14px;font-size:34px;color:var(--bar);letter-spacing:1.5px}
.brand-mark{width:86px;height:86px;border-radius:50%;border:3px solid var(--bar)}
</style>
</head>
<body>
<main class="menu">
  <div class="bar bar-title">PLATOS PRINCIPALES</div>

  <svg width="0" height="0" style="position:absolute">
    <defs>
      <polygon id="burst" points="8,30 30,22 40,6 60,18 82,4 96,16 122,6 110,30 122,48 106,58 112,82 88,72 66,84 48,72 26,80 26,62 4,56 16,44"/>
    </defs>
  </svg>

  <article class="dish" style="left:62px">
    <div class="dish-price">$2.50</div>
    <div class="combo"><svg viewBox="0 0 126 86"><use href="#burst" fill="var(--burst)"/></svg><div class="combo-text"><small>COMBO</small><b>$4.00</b></div></div>
    <div class="photo" role="img" aria-label="Emparedado de queso y jamón en pan flauta sobre papel a cuadros rojos" style="background:linear-gradient(135deg,#8a4a2a,#d8a068 45%,#c2402e)"></div>
    <h2 class="dish-name">A LA PEÑA</h2>
    <p class="dish-desc">Emparedado de queso americano y jamones variados en pan flauta, a la peña.</p>
  </article>

  <article class="dish" style="left:284px">
    <div class="dish-price">$3.00</div>
    <div class="combo"><svg viewBox="0 0 126 86"><use href="#burst" fill="var(--burst)"/></svg><div class="combo-text"><small>COMBO</small><b>$4.50</b></div></div>
    <div class="photo" role="img" aria-label="Choripán con chimichurri, papas fritas y bebida" style="background:linear-gradient(135deg,#7a3a22,#d9b48a 50%,#e0b040)"></div>
    <h2 class="dish-name">BUCOPOCOTÓN</h2>
    <p class="dish-desc">Choripan de chorizo criollo jumbo con chimichurri de la casa en pan baguette.</p>
  </article>

  <article class="dish" style="left:506px">
    <div class="dish-price">$3.25</div>
    <div class="combo"><svg viewBox="0 0 126 86"><use href="#burst" fill="var(--burst)"/></svg><div class="combo-text"><small>COMBO</small><b>$4.75</b></div></div>
    <div class="photo" role="img" aria-label="Patacones con pollo y salsa de ajo sobre fondo azul" style="background:linear-gradient(135deg,#1e3a6e,#d8b040 50%,#1c2f5a)"></div>
    <h2 class="dish-name">MI PATACÓN</h2>
    <p class="dish-desc">Pollo, cebolla caramelizada y salsa de ajo con cilantro sobre cama de patacones.</p>
  </article>

  <article class="dish" style="left:728px">
    <div class="dish-price">$4.50</div>
    <div class="combo"><svg viewBox="0 0 126 86"><use href="#burst" fill="var(--burst)"/></svg><div class="combo-text"><small>COMBO</small><b>$6.00</b></div></div>
    <div class="photo" role="img" aria-label="Emparedado de pollo a la plancha con tomate en pan baguette" style="background:linear-gradient(135deg,#3a2a22,#c89a70 50%,#b83a30)"></div>
    <h2 class="dish-name">EL FAVORITO</h2>
    <p class="dish-desc">Emparedado de pollo a la plancha, queso mozzarella, cebolla caramelizada, tomate y salsa ranch en pan baguette.</p>
  </article>

  <article class="dish" style="left:948px">
    <div class="dish-price">$2.50</div>
    <div class="combo"><svg viewBox="0 0 126 86"><use href="#burst" fill="var(--burst)"/></svg><div class="combo-text"><small>COMBO</small><b>$4.00</b></div></div>
    <div class="photo" role="img" aria-label="Hamburguesa angus con papas fritas en plato blanco" style="background:linear-gradient(135deg,#5a3a20,#c07a38 45%,#e8ddd0)"></div>
    <h2 class="dish-name">LA BOCHINCHOSA</h2>
    <p class="dish-desc">1/2 libra de hamburguesa angus, queso americano, cebolla caramelizada, tomate, bacon y salsa de la casa en pan de miel con semillas de amapola.</p>
  </article>

  <section>
    <div class="bar bar-section" style="left:60px;top:363px;width:348px">ACOMPAÑAMIENTOS</div>
    <div class="row side" style="top:420px"><span>PAPAS FRITAS</span><span>$1.00</span></div>
    <div class="row side" style="top:463px"><span>PATACONES</span><span>$1.00</span></div>
  </section>

  <section>
    <div class="bar bar-section" style="left:60px;top:513px;width:348px">SOPAS</div>
    <div class="photo" role="img" aria-label="Sopa de pollo en vaso con delantal negro de la marca" style="left:112px;top:563px;width:200px;height:103px;background:linear-gradient(135deg,#c8403a,#e8e0cc 45%,#2a2a2a 70%)"></div>
    <div class="row soup" style="top:682px"><span>SOPA DE POLLO CON ARROZ</span><span>$2.95</span></div>
    <div class="row soup" style="top:711px"><span>SOPA DE LENTEJA Y CARNE<br>CON ARROZ</span><span>$2.95</span></div>
  </section>

  <section>
    <div class="bar bar-section" style="left:430px;top:363px;width:348px">PASTELERÍA</div>
    <div class="photo" role="img" aria-label="Hojaldres y pastelitos horneados" style="left:483px;top:413px;width:200px;height:106px;background:linear-gradient(135deg,#2a2a2a,#c88a48 45%,#2a2a2a)"></div>
    <div class="row bakery" style="top:532px"><span>ENCHILADA DE CARNE</span><span>$1.50</span></div>
    <div class="row bakery" style="top:561px"><span>PASTELITO DE POLLO</span><span>$1.25</span></div>
    <div class="row bakery" style="top:590px"><span>PAÑUELO DE QUESO</span><span>$1.00</span></div>
    <div class="row bakery" style="top:619px"><span>CAÑON DE GUAYABA</span><span>$0.85</span></div>
    <div class="row bakery" style="top:648px"><span>DONAS RELLENAS</span><span>$0.85</span></div>
    <p class="note" style="left:445px;top:672px">Crema pastelera, fresa, manzana, maracuyá</p>
    <div class="abs" role="img" aria-label="Ilustración de camión de comida" style="left:510px;top:692px;width:176px;height:72px;border-radius:10px 10px 6px 6px;background:linear-gradient(180deg,#c8403a 0 14%,#3a3a3a 14%)"></div>
  </section>

  <section>
    <div class="bar bar-section" style="left:797px;top:363px;width:348px">BEBIDAS</div>
    <div class="row drink" style="top:405px"><span>CHICHEME CHORRERANO (16OZ)</span><span>$1.60</span></div>
    <div class="row drink" style="top:434px"><span>CHICA DEL DÍA (16OZ)</span><span>$1.00</span></div>
    <div class="row drink" style="top:463px"><span>CAFÉ DE ALTURA (8OZ)</span><span>$1.00</span></div>
    <div class="row drink" style="top:492px"><span>AGUA (16OZ)</span><span>$0.75</span></div>
    <div class="row drink" style="top:521px"><span>SODAS (12OZ)</span><span>$1.00</span></div>
    <p class="note" style="left:812px;top:548px">Cola Roja, Cola Cero, Frescura, Tropi Fresa, Tropi Manzana</p>
  </section>

  <div class="abs" role="img" aria-label="Ilustración a línea del horizonte de la ciudad" style="left:800px;top:580px;width:370px;height:192px;background:linear-gradient(180deg,rgba(90,60,30,0) 0%,rgba(90,60,30,.08) 100%)"></div>
  <div class="brand"><span>PAN DORADO</span><span class="brand-mark"></span></div>
</main>
</body>
</html>
```